Designing a website that functions as the shop window for the various aspects of my business -...

I need a website, with separate webpages covering the different components of my practice (small animal consultancy, equine behaviour consultancy, legal case work and education provider). I have a website (www.petmindstudio.ie) but I haven't updated it in recent years to reflect the newer developments / aspects of my business. Most of my work has been in Ireland but I would like to begin to create an international profile, particularly with regard to the legal casework and offering education within the international horse industry. My overall goal is to improve understanding of animals and animal behaviour, and by doing so, help to reduce the performance of behaviour problems, and also improve animal welfare as a result.

Target Market(s)

Horse and dog owners, horse riders, veterinary surgeons, solicitors

Industry/Entity Type

Legal

Logo Text

Text to be decided on

Number of Pages Required

5+ page

Font styles to use
Sans Serif
Decorative
Script

Colors

Designer to choose colors to be used in the design.

Requirements
Must have
• Relevant content from the attached Flyer including photos
• Use of the phrases:
• 'Understanding Animals'
• Improving animals lives through better understanding
• Science-based, up-to-date relevant information regarding animal behaviour
Nice to have
• 'Leading professional service educating people in understanding animals'
• Separate pages for 1) About, 2) Canine and Feline behaviour Consultancy 3) Equine Consultancy 4) Legal expert witness Consultancy 5) Education 6, FAQs
Should not have
• Prices of services (as these may change from time to time)

```html
<!DOCTYPE html>
<html lang="en">
<head>
<meta charset="utf-8">
<title>Legal Expert Witness Consultancy – Pet Mind Studio</title>
<link rel="stylesheet" href="https://fonts.googleapis.com/css2?family=Lato:wght@400;700&family=Caveat+Brush&display=swap">
<style>
:root{
  --green:#078a52;
  --red:#e0202c;
  --ink:#222;
  --grey-bg:#f3f3f3;
  --footer-bg:#1f1c1d;
  --footer-text:#e6e6e6;
  --white:#fff;
}
*{box-sizing:border-box;margin:0;padding:0}
html,body{width:1148px;height:1200px;overflow:hidden}
body{font-family:'Lato',sans-serif;color:var(--ink);background:var(--white);position:relative}
.container{position:absolute;left:136px;width:876px}

/* header */
.site-header{position:absolute;top:0;left:0;width:1148px;height:78px;background:var(--grey-bg)}
.header-phone{position:absolute;left:136px;top:20px;display:flex;align-items:center;gap:13px;font-size:15px;color:#333}
.icon-circle{width:32px;height:32px;border-radius:50%;background:var(--red);display:flex;align-items:center;justify-content:center}
.brand{position:absolute;left:420px;top:20px;display:flex;align-items:center;gap:12px;font-size:26px;font-weight:700;color:var(--green)}
.brand-dot{width:30px;height:30px;border-radius:50%;background:var(--green)}
.header-login{position:absolute;left:927px;top:21px;display:flex;align-items:center;gap:14px;font-size:15px;color:#333}

/* nav */
.main-nav{position:absolute;top:78px;left:0;width:1148px;height:34px;background:var(--green)}
.main-nav ul{list-style:none;position:absolute;left:135px;top:0;display:flex;height:34px}
.main-nav li{display:flex;align-items:center;justify-content:center;height:34px;color:var(--white);font-size:12px;border-right:1px solid rgba(255,255,255,.15)}
.main-nav li:last-child{border-right:none}
.main-nav li.active{background:var(--red)}

/* hero */
.hero{position:absolute;top:112px;left:0;width:1148px;height:304px;background:linear-gradient(180deg,#c9d2c4 0%,#dfe3da 45%,#cdd6c2 100%)}
.hero-horses{position:absolute;right:0;top:0;width:399px;height:304px;background:radial-gradient(ellipse at 55% 55%,#a4552a 0%,#8a3f1c 45%,rgba(200,190,170,0) 80%)}
.hero-title{position:absolute;left:136px;top:78px;font-family:'Caveat Brush',cursive;font-size:41px;line-height:48px;color:var(--green)}
.hero-title .accent{color:var(--red)}

/* breadcrumb */
.breadcrumb{position:absolute;top:416px;left:0;width:1148px;height:34px;background:var(--grey-bg)}
.breadcrumb p{position:absolute;left:136px;top:10px;font-size:12px;color:var(--ink)}
.breadcrumb .sep{margin:0 8px;color:#555}
.breadcrumb .current{color:var(--red)}

/* content */
.section-title{position:absolute;top:514px;left:0;width:1148px;display:flex;justify-content:center;align-items:center;gap:18px}
.section-title .title-dot{width:22px;height:22px;border-radius:50%;background:var(--green)}
.section-title h1{font-family:'Caveat Brush',cursive;font-weight:400;font-size:26px;color:var(--green)}
.content-text{position:absolute;left:138px;top:589px;width:468px;font-size:11.6px;line-height:21.9px;text-align:justify}
.content-text p+p{margin-top:8px}
.content-photo{position:absolute;left:641px;top:588px;width:371px;height:260px;border-radius:5px;background:linear-gradient(180deg,#5f8d3a 0%,#7ea54c 45%,#9ab35c 100%)}

/* footer */
.site-footer{position:absolute;top:915px;left:0;width:1148px;height:251px;background:linear-gradient(180deg,#242122 0%,#2b2322 60%,#3a2a22 100%);color:var(--footer-text)}
.footer-col{position:absolute;top:41px}
.footer-col h3{font-size:13px;font-weight:700;color:var(--white);padding-bottom:8px;border-bottom:1px solid rgba(255,255,255,.2);position:relative;text-transform:uppercase}
.footer-col h3 span{color:var(--green);font-weight:400}
.footer-col h3::after{content:"";position:absolute;left:0;bottom:-1px;width:30px;height:2px;background:var(--green)}
.quick-links{left:136px;width:92px}
.quick-links ul{list-style:none;margin-top:14px;font-size:10.5px;line-height:14px}
.quick-links li{padding-left:10px;position:relative;margin-bottom:6px}
.quick-links li::before{content:"›";position:absolute;left:0;top:-1px;color:#aaa}
.contact{left:316px;width:197px}
.contact .row{display:flex;gap:10px;font-size:10.5px;line-height:16px;margin-top:14px}
.contact .row:first-of-type{margin-top:16px}
.contact .row+.row{margin-top:18px}
.contact strong{color:var(--white)}
.follow{left:568px;width:147px}
.follow .item{display:flex;align-items:center;gap:22px;font-size:10.5px;margin-top:10px}
.follow .item:first-of-type{margin-top:14px}
.social-dot{width:27px;height:27px;border-radius:50%}
.social-dot.red{background:var(--red)}
.social-dot.blue{background:#1a67c9}
.social-dot.sky{background:#2a9ee6}
.hours{left:771px;width:241px}
.hours table{border-collapse:collapse;margin-top:10px;font-size:10.5px;width:100%}
.hours td{padding:4.6px 0;vertical-align:top}
.hours td.colon{width:30px}
.hours td.dash{width:12px;text-align:center}
.footer-divider{position:absolute;top:41px;width:1px;height:175px;background:rgba(255,255,255,.12)}
.copyright{position:absolute;top:1166px;left:0;width:1148px;height:34px;background:var(--green);color:var(--white);font-size:10.5px;display:flex;align-items:center;justify-content:center}
</style>
</head>
<body>

<header class="site-header">
  <div class="header-phone">
    <span class="icon-circle"><svg width="14" height="14" viewBox="0 0 24 24"><path fill="#fff" d="M6.6 10.8a15 15 0 0 0 6.6 6.6l2.2-2.2c.3-.3.7-.4 1-.2 1.1.4 2.3.6 3.6.6.6 0 1 .4 1 1V20c0 .6-.4 1-1 1A17 17 0 0 1 3 4c0-.6.4-1 1-1h3.5c.6 0 1 .4 1 1 0 1.3.2 2.5.6 3.6.1.3 0 .7-.2 1z"/></svg></span>
    01 555 0148
  </div>
  <div class="brand"><span class="brand-dot"></span>Pet Mind Studio</div>
  <div class="header-login">
    <span class="icon-circle"><svg width="14" height="14" viewBox="0 0 24 24"><path fill="#fff" d="M10 6l6 6-6 6v-4H3v-4h7zM14 3h6a1 1 0 0 1 1 1v16a1 1 0 0 1-1 1h-6v-2h5V5h-5z"/></svg></span>
    Login
  </div>
</header>

<nav class="main-nav">
  <ul>
    <li style="width:35px"><svg width="14" height="13" viewBox="0 0 24 22"><path fill="#fff" d="M12 1 1 11h3v10h6v-6h4v6h6V11h3z"/></svg></li>
    <li style="width:70px">About</li>
    <li style="width:252px">Canine &amp; Feline behaviour Consultancy</li>
    <li style="width:149px">Equine Consultancy</li>
    <li class="active" style="width:220px">Legal expert witness Consultancy</li>
    <li style="width:96px">Education</li>
    <li style="width:62px">FAQs</li>
  </ul>
</nav>

<section class="hero" role="img" aria-label="Farm landscape with paddock fence and red barn, two chestnut horses nuzzling on the right">
  <div class="hero-horses"></div>
  <h2 class="hero-title">Our Goal Is To Improve<br>Understanding <span class="accent">of Animals</span><br><span class="accent">&amp; Animal Behaviour</span></h2>
</section>

<div class="breadcrumb"><p>Home<span class="sep">›</span><span class="current">Legal Expert Witness Consultancy</span></p></div>

<div class="section-title"><span class="title-dot"></span><h1>Legal Expert Witness Consultancy</h1></div>

<div class="content-text">
  <p>Part of our work at the Pet Mind Studio is in offering expert opinion evidence for court cases involving animal behaviour. Many legal cases deal with issues surrounding the behaviour of animals such as aggression in dogs, injuries occurring around horses, poor care of animals and others. In these cases, the scientific and veterinary knowledge of normal and behaviour patterns of animals, and the factors influencing behaviour at all stages during life help in bringing clarity to issues where clear answers are required, such as in the courtroom.</p>
  <p>We have extensive experience of drawing up court reports, and making comment on liability in civil cases. We can attend the site of an incident to assess all pertinent features of the environment, and draw up a detailed, scientific and clear report for use in court. We can also appear to give verbal testimony in court when required.</p>
</div>
<div class="content-photo" role="img" aria-label="Young chestnut foal standing in a green meadow with trees behind"></div>

<footer class="site-footer" role="img" aria-label="Dark city skyline at dusk behind the footer">
  <div class="footer-col quick-links">
    <h3><span>Quick</span> Links</h3>
    <ul>
      <li>About</li>
      <li>Canine &amp; Feline Behaviour Consultancy</li>
      <li>Equine Consultancy</li>
      <li>Legal expert witness Consultancy</li>
      <li>Education</li>
      <li>FAQs</li>
    </ul>
  </div>
  <div class="footer-divider" style="left:284px"></div>
  <div class="footer-col contact">
    <h3><span>Contact</span> Details</h3>
    <div class="row"><svg width="12" height="14" viewBox="0 0 24 28"><path fill="#078a52" d="M12 0a9 9 0 0 0-9 9c0 7 9 19 9 19s9-12 9-19a9 9 0 0 0-9-9zm0 12.5A3.5 3.5 0 1 1 12 5.5a3.5 3.5 0 0 1 0 7z"/></svg><div><strong>Pet Mind Studio</strong><br>48 Meadow Lane, Unit 7 Kilbrook<br>KB 204816</div></div>
    <div class="row"><svg width="12" height="12" viewBox="0 0 24 24"><path fill="#078a52" d="M6.6 10.8a15 15 0 0 0 6.6 6.6l2.2-2.2c.3-.3.7-.4 1-.2 1.1.4 2.3.6 3.6.6.6 0 1 .4 1 1V20c0 .6-.4 1-1 1A17 17 0 0 1 3 4c0-.6.4-1 1-1h3.5c.6 0 1 .4 1 1 0 1.3.2 2.5.6 3.6.1.3 0 .7-.2 1z"/></svg><div>01 555 0148</div></div>
    <div class="row"><svg width="13" height="11" viewBox="0 0 24 18"><path fill="#078a52" d="M0 0h24v2L12 10 0 2zm0 4 12 8 12-8v14H0z"/></svg><div>hello@petmindstudio.ie</div></div>
  </div>
  <div class="footer-divider" style="left:536px"></div>
  <div class="footer-col follow">
    <h3><span>Follow</span> Us</h3>
    <div class="item"><span class="social-dot red"></span>Reviews</div>
    <div class="item"><span class="social-dot blue"></span>Community</div>
    <div class="item"><span class="social-dot sky"></span>Updates</div>
    <div class="item"><span class="social-dot red"></span>Videos</div>
  </div>
  <div class="footer-divider" style="left:739px"></div>
  <div class="footer-col hours">
    <h3><span>Opening</span> Hours</h3>
    <table>
      <tr><td>Monday</td><td class="colon">:</td><td>9:30 am</td><td class="dash">-</td><td>6:00 pm</td></tr>
      <tr><td>Tuesday</td><td class="colon">:</td><td>9:30 am</td><td class="dash">-</td><td>6:00 pm</td></tr>
      <tr><td>Wednesday</td><td class="colon">:</td><td>9:30 am</td><td class="dash">-</td><td>6:00 pm</td></tr>
      <tr><td>Thursday</td><td class="colon">:</td><td>9:30 am</td><td class="dash">-</td><td>6:00 pm</td></tr>
      <tr><td>Friday</td><td class="colon">:</td><td>9:30 am</td><td class="dash">-</td><td>6:00 pm</td></tr>
      <tr><td>Saturday &amp; Sunday</td><td class="colon">:</td><td>Off</td><td></td><td></td></tr>
    </table>
  </div>
</footer>

<div class="copyright">Copyright © 2019 Pet Mind Studio. All Rights Reserved.</div>

</body>
</html>
```